Premium Lawn fertiliser packaging - Looking for long term designer

*Update at bottom
I need a carefully considered, bold and professional packaging design for my new premium lawn fertiliser product. This contest is for a detailed front of the stand-up pouch packaging and once I’ve chosen a winner, they’ll be asked to create the layout for the back that links to the front as well. I have a full range of additional products that will also need designs and so I'm looking for someone who can do a great job here and who we can work with long term.

The front should include our logo for Pemberly Turf Supply Direct and be titled “Bloom Vigor Max” "Professional Lawn Fertiliser". The spring fertiliser tag line is "Awaken your lawn: Lush Greening, Lasting Health".
Beneath it, it then needs to include some important usage information and the key benefits along with some suitable graphic.

Key information to include:

Apply March - June
Treats 35-50 m2
16-3-8
+2%MgO + 1% Fe + 2.9% CaO (this is the chemical makeup of the fertiliser and needs to be fairly prominent. If you look at other professional fertiliser packaging, you'll see how it needs to compare).

Key features:
Premium fertiliser, used by professionals
Advanced greening with micro-nutrient complex
Dual action Nitrogen: Instant green boost & continuous feed for 3 months
Child & pet safe

Our brand colours are purple and green. Purple = #592999, Green = 3cb64a / 81d742 / 4d9d44

I think these colours look great against a white background.

Please make sure you look at our website as well to get an idea of our brand: www.pemberlyturfsupply.co.uk

To help, I've attached images of competitors fertiliser packaging that I like the look of. I'm not looking for you to copy but just see what type of thing appeals to me, the standard I'm expecting and what I need to compete against....

In addition, I have also attached some potential images you may wish to try using in your design, although please feel free to use your own if you have something better. For the moment, the images are 'preview' images, but once I decide on a design and we agree on the correct image, I will download and send over a fully licensed version.

*** Update*** When submitting your design, can you submit it in 2 formats: The first as a fully printed custom stand-up pouch and the second as a full-size label stuck onto a standup pouch (whatever colour you think is right for your design - choose white if you are not sure). To explain, I've just discovered we won't be able to get full custom bags printed in time for the first run and so we will have to opt for the design to be printed on labels and fixed onto bags. I therefore need to choose a design that works in both formats as both a label on a standup pouch as well as a fully printed pouch. Many thanks.

Target Market(s)

Domestic home-owners

Industry/Entity Type

Lawn care. NOT AGRICULTURE OR FARMING

Font styles to use
Sans Serif

Requirements
Must have
• Presented in 2 formats - see update at bottom of description
Nice to have
• I quite like designs against a white background, although I’m open to other ideas as well.
Should not have
• Please do not include any people or faces in the design. The text should be solid in colour, so no graduated colour fill in the text or outline text. Please avoid over-busy or cluttered designs.

```html
<!DOCTYPE html>
<html lang="en">
<head>
<meta charset="utf-8">
<title>Bloom Vigor Max – Professional Lawn Fertiliser Label</title>
<link href="https://fonts.googleapis.com/css2?family=Anton&family=Syncopate:wght@700&family=Montserrat:wght@300;400;500;600;700&display=swap" rel="stylesheet">
<style>
  :root {
    --stage: #6a7f50;
    --grass-dark: #1f4a1c;
    --grass-mid: #2f6a26;
    --grass-deep: #153612;
    --lime: #9fd12c;
    --lime-light: #c8e84a;
    --title-green: #8ccf2e;
    --brown: #3a2418;
    --white: #ffffff;
    --icon-green: #4d9d44;
    --ink: #2a1a12;
    --photo-sky: #9fb6a0;
    --photo-lawn: #6ea22a;
  }
  * { box-sizing: border-box; margin: 0; padding: 0; }
  html, body { width: 1200px; height: 2400px; overflow: hidden; background: var(--stage); }
  .stage { position: relative; width: 1200px; height: 2400px; }
  .label {
    position: absolute; left: 50px; top: 267px;
    width: 632px; height: 1072px;
    transform: scale(1.7405); transform-origin: 0 0;
    overflow: hidden; font-family: "Montserrat", sans-serif; color: var(--white);
    box-shadow: 0 4px 14px rgba(0,0,0,.35);
  }
  .label__photo {
    position: absolute; inset: 0 0 auto 0; height: 340px;
    background: linear-gradient(180deg, var(--photo-sky) 0%, #7f9a63 22%, var(--photo-lawn) 45%, #9ccf36 75%, #7fb22a 100%);
  }
  .label__shapes { position: absolute; inset: 0; }
  .logo {
    position: absolute; left: 194px; top: 132px; width: 256px; height: 256px;
    border-radius: 50%; background: var(--white); border: 5px solid var(--brown);
    display: flex; align-items: center; justify-content: center; text-align: center;
  }
  .logo__name {
    font-family: "Montserrat", sans-serif; font-weight: 700; font-size: 27px; line-height: 1.15;
    color: var(--brown); width: 200px;
  }
  .title {
    position: absolute; left: 0; right: 0; top: 396px; text-align: center;
    font-family: "Anton", sans-serif; font-size: 70px; line-height: 1; color: var(--title-green);
    letter-spacing: 0.5px;
  }
  .subtitle {
    position: absolute; left: 0; right: 0; top: 478px; text-align: center;
    font-family: "Syncopate", sans-serif; font-weight: 700; font-size: 30px; line-height: 1;
  }
  .product-type {
    position: absolute; left: 82px; top: 518px; width: 480px; height: 46px;
    background: var(--white); color: var(--brown);
    font-family: "Syncopate", sans-serif; font-weight: 700; font-size: 31px;
    display: flex; align-items: center; justify-content: center;
  }
  .tagline {
    position: absolute; left: 0; right: 0; top: 580px; text-align: center;
    font-weight: 400; font-size: 23px; line-height: 27px; letter-spacing: 3.5px;
  }
  .features { position: absolute; left: 60px; top: 654px; width: 520px; display: flex; }
  .feature { flex: 1; text-align: center; font-size: 13.5px; line-height: 16px; padding: 0 4px; }
  .feature + .feature { border-left: 1px solid rgba(255,255,255,.25); }
  .feature__icon { display: block; margin: 0 auto 16px; }
  .feature strong { font-weight: 700; }
  .label__lawn-base {
    position: absolute; left: 0; right: 0; bottom: 0; height: 300px;
    background: radial-gradient(ellipse at 50% 30%, var(--lime-light) 0%, var(--lime) 45%, #6fa61c 100%);
  }
  .safety-badge { position: absolute; left: 80px; top: 866px; }
  .usage { position: absolute; left: 170px; top: 898px; width: 392px; }
  .usage__season { font-family: "Syncopate", sans-serif; font-weight: 700; font-size: 20px; color: var(--brown); padding-left: 18px; }
  .usage__formula {
    margin-top: 6px; height: 30px; background: var(--grass-deep); color: var(--white);
    font-family: "Syncopate", sans-serif; font-weight: 700; font-size: 17px;
    display: flex; align-items: center; justify-content: center;
  }
  .specs { position: absolute; left: 0; right: 0; top: 970px; display: flex; justify-content: center; gap: 26px; font-size: 19px; font-weight: 500; color: var(--ink); }
  .specs span { display: inline-flex; align-items: center; gap: 4px; }
  .net { position: absolute; left: 0; right: 0; top: 1005px; text-align: center; font-size: 15px; font-weight: 500; color: var(--brown); }
  .net b { font-size: 23px; font-weight: 700; color: var(--white); }
  .net small { font-size: 14px; font-weight: 700; color: var(--white); }
</style>
</head>
<body>
<div class="stage">
  <div class="label">
    <div class="label__photo" role="img" aria-label="Sunlit close-up of a lush green lawn with a blurred house and trees behind"></div>
    <div class="label__lawn-base" role="img" aria-label="Bright lime-green grass close-up"></div>
    <svg class="label__shapes" width="632" height="1072" viewBox="0 0 632 1072" role="img" aria-label="Dark green grass texture panel">
      <defs>
        <radialGradient id="panelGrass" cx="50%" cy="40%" r="70%">
          <stop offset="0" stop-color="#2f6a26"/>
          <stop offset="0.6" stop-color="#1f4a1c"/>
          <stop offset="1" stop-color="#122e10"/>
        </radialGradient>
      </defs>
      <path d="M0,205 Q316,335 632,205 L632,900 Q316,770 0,900 Z" fill="url(#panelGrass)"/>
      <path d="M0,198 Q316,328 632,198" fill="none" stroke="#3a2418" stroke-width="10"/>
      <path d="M0,193 Q316,323 632,193" fill="none" stroke="#ffffff" stroke-width="2"/>
      <path d="M70,855 Q316,760 562,855" fill="none" stroke="#ffffff" stroke-width="5"/>
    </svg>

    <div class="logo"><span class="logo__name">Pemberly Turf Supply Direct</span></div>

    <h1 class="title">BLOOM VIGOR MAX</h1>
    <p class="subtitle">PROFESSIONAL</p>
    <p class="product-type">LAWN FERTILISER</p>
    <p class="tagline">AWAKEN YOUR LAWN<br>LUSH GREENING, LASTING HEALTH</p>

    <div class="features">
      <div class="feature">
        <svg class="feature__icon" width="46" height="46" viewBox="0 0 46 46"><circle cx="23" cy="23" r="23" fill="#4d9d44"/><path d="M14,19 L18,14 H28 L32,19 L23,31 Z M14,19 H32 M18,14 L23,31 L28,14" fill="none" stroke="#fff" stroke-width="1.5" stroke-linejoin="round"/></svg>
        <strong>Premium fertiliser</strong><br>used by<br>professionals
      </div>
      <div class="feature">
        <svg class="feature__icon" width="46" height="46" viewBox="0 0 46 46"><circle cx="23" cy="23" r="23" fill="#4d9d44"/><path d="M13,31 Q14,22 11,16 M18,31 Q18,20 16,13 M23,31 V12 M28,31 Q28,20 30,13 M33,31 Q32,22 35,16 M11,31 H35" fill="none" stroke="#fff" stroke-width="1.6" stroke-linecap="round"/></svg>
        <strong>Advanced greening</strong><br>with micro-nutrient<br>complex
      </div>
      <div class="feature">
        <svg class="feature__icon" width="46" height="46" viewBox="0 0 46 46"><circle cx="23" cy="23" r="23" fill="#4d9d44"/><path d="M12,28 H20 Q24,28 26,30 H32 M12,33 H30 L35,28 M24,26 V17 M24,20 Q18,19 18,13 Q24,13 24,20 M24,18 Q28,12 32,14 Q30,19 24,18" fill="none" stroke="#fff" stroke-width="1.5" stroke-linecap="round" stroke-linejoin="round"/></svg>
        <strong>Dual action Nitrogen:</strong><br>Instant green boost &amp;<br>continuous feed<br>for 3 months
      </div>
    </div>

    <svg class="safety-badge" width="92" height="110" viewBox="0 0 92 110" role="img" aria-label="Child and pet safe badge">
      <path d="M46,3 L88,16 V52 Q88,88 46,107 Q4,88 4,52 V16 Z" fill="#4d9d44" stroke="#153612" stroke-width="5"/>
      <path d="M46,12 L80,22 V52 Q80,82 46,98 Q12,82 12,52 V22 Z" fill="#153612"/>
    </svg>

    <div class="usage">
      <p class="usage__season">APPLY MARCH - JUNE</p>
      <p class="usage__formula">+2%MGO + 1% FE + 2.9% CAO</p>
    </div>

    <div class="specs">
      <span><svg width="18" height="18" viewBox="0 0 18 18"><path d="M2,10 L7,15 L16,2" fill="none" stroke="#8a2b12" stroke-width="3" stroke-linecap="round" stroke-linejoin="round"/></svg>Treats 35-50 m2</span>
      <span><svg width="18" height="18" viewBox="0 0 18 18"><path d="M2,10 L7,15 L16,2" fill="none" stroke="#8a2b12" stroke-width="3" stroke-linecap="round" stroke-linejoin="round"/></svg>16-3-8</span>
    </div>

    <p class="net">NETWT. <b>10</b><small>LBS</small> &nbsp; COVERS UP TO <b>2500</b><small>SQFT.</small></p>
  </div>
</div>
</body>
</html>
```